Security Warning Sign

We have an existing sign that needs an update. I have attached a picture of the current square sign. We need to maintain the same wording. It needs to be professional and appropriate to attach to our customers fence. Also attached is a copy of our building sign which may lend some inspiration and hopefully the ai format will assist. The final sign will be 600mm x 600mmOur website is www.halvorngate.com.au

```html
<!DOCTYPE html>
<html lang="en">
<head>
<meta charset="utf-8">
<title>Security Warning Sign</title>
<link rel="stylesheet" href="https://fonts.googleapis.com/css2?family=Arimo:wght@700&family=Oswald:wght@700&display=swap">
<style>
  :root {
    --red: #ec3237;
    --ink: #231f20;
    --orange: #f38a33;
    --white: #ffffff;
    --camera-light: #f1f1f1;
    --camera-dark: #bdbdbd;
  }
  * { margin: 0; padding: 0; box-sizing: border-box; }
  html, body { width: 1200px; height: 1199px; overflow: hidden; background: var(--white); }
  .sign { position: relative; width: 1200px; height: 1199px; background: var(--white); overflow: hidden; }

  .warning-band {
    position: absolute; left: 0; top: 5px; width: 1200px; height: 203px;
    background: var(--red);
    display: flex; align-items: center; justify-content: center;
  }
  .warning-title {
    font-family: "Arimo", Arial, sans-serif; font-weight: 700;
    color: var(--white); font-size: 210px; line-height: 1; letter-spacing: 1px;
    margin-top: 4px;
  }

  .camera-illustration {
    position: absolute; left: 211px; top: 252px; width: 642px; height: 370px;
    background: linear-gradient(160deg, var(--camera-light) 0%, var(--camera-dark) 100%);
    border-radius: 6px;
  }

  .notice {
    position: absolute; left: 0; top: 655px; width: 1178px;
    font-family: "Arimo", Arial, sans-serif; font-weight: 700;
    color: var(--ink); font-size: 77px; line-height: 86.5px;
    text-align: center; letter-spacing: 0.5px;
  }
  .notice .accent { color: var(--red); }

  .footer-rule {
    position: absolute; left: 1px; top: 1016px; width: 1198px; height: 5px;
    background: var(--orange);
  }

  .brand-mark {
    position: absolute; left: 28px; top: 1060px; width: 230px; height: 120px;
    display: flex; align-items: center; gap: 12px;
  }
  .brand-dot { width: 46px; height: 46px; border-radius: 50%; background: var(--orange); flex: none; }
  .brand-name {
    font-family: "Oswald", "Arial Narrow", sans-serif; font-weight: 700;
    font-size: 64px; color: var(--ink); letter-spacing: 1px;
  }

  .company-name {
    position: absolute; left: 325px; top: 1074px; width: 430px;
    font-family: "Oswald", "Arial Narrow", sans-serif; font-weight: 700;
    font-size: 40px; line-height: 56px; color: var(--ink);
    text-align: center; letter-spacing: 0;
    white-space: nowrap;
  }

  .contact { position: absolute; left: 770px; width: 430px; }
  .contact-phone { top: 1043px; height: 82px; }
  .contact-web { top: 1133px; height: 58px; }
  .contact svg.band { position: absolute; inset: 0; width: 100%; height: 100%; }
  .contact-content {
    position: absolute; display: flex; align-items: center; gap: 12px;
    font-family: "Oswald", "Arial Narrow", sans-serif; font-weight: 700; color: var(--white);
  }
  .contact-phone .contact-content { left: 68px; top: 0; height: 82px; font-size: 46px; letter-spacing: 1px; }
  .contact-web .contact-content { left: 52px; top: 0; height: 58px; font-size: 21px; }
</style>
</head>
<body>
<main class="sign">
  <header class="warning-band">
    <h1 class="warning-title">WARNING</h1>
  </header>

  <div class="camera-illustration" role="img" aria-label="Illustration of a wall-mounted CCTV security camera with a red lens panel"></div>

  <p class="notice">
    ELECTRONIC<br>
    <span class="accent">SURVEILLANCE</span> AND<br>
    <span class="accent">RECORDING</span> DEVICES<br>
    INSTALLED IN THIS AREA.
  </p>

  <div class="footer-rule"></div>

  <div class="brand-mark">
    <span class="brand-dot"></span>
    <span class="brand-name">HGS</span>
  </div>

  <p class="company-name">HALVORNGATE SECURITY<br>SERVICES</p>

  <div class="contact contact-phone">
    <svg class="band" viewBox="0 0 430 82" preserveAspectRatio="none" aria-hidden="true">
      <polygon points="0,82 50,0 58,0 8,82" fill="var(--orange)"/>
      <polygon points="20,82 70,0 430,0 430,82" fill="var(--orange)"/>
    </svg>
    <div class="contact-content">
      <svg width="40" height="40" viewBox="0 0 24 24" aria-hidden="true">
        <path fill="#fff" d="M6.6 10.8a15.1 15.1 0 0 0 6.6 6.6l2.2-2.2a1 1 0 0 1 1-.25 11.4 11.4 0 0 0 3.6.57 1 1 0 0 1 1 1V20a1 1 0 0 1-1 1A17 17 0 0 1 3 4a1 1 0 0 1 1-1h3.5a1 1 0 0 1 1 1c0 1.250.2 2.450.57 3.6a1 1 0 0 1-.25 1z"/>
      </svg>
      <span>1300 555 014</span>
    </div>
  </div>

  <div class="contact contact-web">
    <svg class="band" viewBox="0 0 430 58" preserveAspectRatio="none" aria-hidden="true">
      <polygon points="0,58 46,0 56,0 10,58" fill="var(--orange)"/>
      <polygon points="22,58 68,0 430,0 430,58" fill="var(--orange)"/>
    </svg>
    <div class="contact-content">
      <svg width="32" height="32" viewBox="0 0 24 24" aria-hidden="true">
        <g fill="none" stroke="#fff" stroke-width="1.8">
          <circle cx="12" cy="12" r="10"/>
          <ellipse cx="12" cy="12" rx="4.5" ry="10"/>
          <line x1="2" y1="12" x2="22" y2="12"/>
        </g>
      </svg>
      <span>WWW.HALVORNGATE.COM.AU</span>
    </div>
  </div>
</main>
</body>
</html>
```